Business card design Needed for new logo / Construction business, home extensions and new builds

We need a business card design using our new logo files which i will attach to this project :)

We are a small construction business specialising in home extensions, new builds and property development. We are very ambitious and would appreciate professional and elegant designs for our new business card.

Very serious about using the services on Sketchwharf and recently acquired our new logo from here :)

Please get involved, i will feedback when i can as i am very busy but can respond daily, thanks

Target Market(s)

People that want to build onto their houses, new building developments or adding too their existing property

Industry/Entity Type

Construction

Contact Information for Business Card

Thornley Pike Construction, Wilbur Fenwick (Managing Director), Tel 07829456172, email - info@thornley-pike, www.thornley-pike.co.uk

Colors

Designer to choose colors to be used in the design.

Requirements
Must have
• I like a deep grey on the back please. A lot of you have provided black from and back, try mixing things up a little. The black looks cool 😎 Thanks

```html
<!DOCTYPE html>
<html lang="en">
<head>
<meta charset="utf-8">
<title>Thornley Pike Construction – Business Card</title>
<link rel="stylesheet" href="https://fonts.googleapis.com/css2?family=Arimo:wght@400;700&display=swap">
<style>
  :root {
    --backdrop: #e4e4e2;
    --card: #2b2b2b;
    --card-deep: #262626;
    --gold: #d9a520;
    --gold-light: #f2c94c;
    --silver: #d8d8d8;
    --text: #f2f2f2;
    --pattern-dark: #222222;
    --pattern-light: #3a3a3a;
  }
  * { margin: 0; padding: 0; box-sizing: border-box; }
  html, body {
    width: 1200px; height: 801px; overflow: hidden;
    background: var(--backdrop);
    font-family: "Arimo", Arial, sans-serif;
  }
  .stage {
    width: 1200px; height: 801px;
    display: flex; align-items: center; justify-content: center; gap: 40px;
  }
  .card {
    position: relative;
    width: 540px; height: 309px;
    background: var(--card);
    box-shadow: 0 6px 18px rgba(0,0,0,.18);
    overflow: hidden;
  }
  /* Front */
  .brand {
    position: absolute; top: 44px; right: 40px;
    display: flex; align-items: center; gap: 12px;
  }
  .brand-mark { width: 26px; height: 26px; background: var(--gold); flex: none; }
  .brand-name {
    color: var(--silver); font-weight: 700; font-size: 19px;
    letter-spacing: 1.5px; text-transform: uppercase; line-height: 1.25;
    text-align: left;
  }
  .person { position: absolute; left: 34px; top: 116px; }
  .person-name {
    color: var(--gold-light); font-weight: 700; font-size: 21px; letter-spacing: .5px;
  }
  .person-role { color: var(--text); font-size: 14px; margin-top: 2px; }
  .gold-rule {
    position: absolute; left: 30px; right: 30px; top: 168px;
    height: 1px; background: var(--gold);
  }
  .contacts {
    position: absolute; left: 34px; top: 190px;
    list-style: none; color: var(--text); font-size: 14px;
  }
  .contacts li { display: flex; align-items: center; gap: 10px; height: 24px; white-space: nowrap; }
  .contacts svg { width: 14px; height: 14px; flex: none; }
  .address {
    position: absolute; right: 34px; top: 190px;
    color: var(--text); font-size: 14px; line-height: 1.5; text-align: right;
    white-space: nowrap;
  }
  /* Back */
  .card-back { background: var(--card-deep); }
  .pattern {
    position: absolute; inset: 0;
    background: linear-gradient(120deg, var(--pattern-dark) 0%, var(--card-deep) 45%, var(--pattern-light) 100%);
  }
  .back-brand {
    position: absolute; right: 40px; bottom: 70px;
    display: flex; align-items: center; gap: 12px;
  }
</style>
</head>
<body>
<main class="stage">
  <section class="card card-front">
    <div class="brand">
      <span class="brand-mark"></span>
      <span class="brand-name">Thornley Pike<br>Construction</span>
    </div>
    <div class="person">
      <div class="person-name">HOLLIS BRANT</div>
      <div class="person-role">Manager</div>
    </div>
    <div class="gold-rule"></div>
    <ul class="contacts">
      <li>
        <svg viewBox="0 0 16 16"><path d="M4 1.5l2.5 3-1.5 1.5c.8 1.8 2.2 3.2 4 4l1.5-1.5 3 2.5-1.5 2.5C7 13 3 9 1.5 3.5z" fill="var(--gold)"/></svg>
        07829 456172
      </li>
      <li>
        <svg viewBox="0 0 16 16"><rect x="1.5" y="3.5" width="13" height="9" fill="none" stroke="var(--gold)" stroke-width="1.4"/><path d="M1.5 3.5l6.5 5 6.5-5" fill="none" stroke="var(--gold)" stroke-width="1.4"/></svg>
        info@thornley-pike.co.uk
      </li>
      <li>
        <svg viewBox="0 0 16 16"><circle cx="8" cy="8" r="6.5" fill="none" stroke="var(--gold)" stroke-width="1.4"/><ellipse cx="8" cy="8" rx="2.8" ry="6.5" fill="none" stroke="var(--gold)" stroke-width="1.2"/><path d="M1.5 8h13" stroke="var(--gold)" stroke-width="1.2"/></svg>
        www.thornley-pike.co.uk
      </li>
    </ul>
    <div class="address">14 Harrow Lane, Leeds<br>West Yorkshire, LS6 2QT</div>
  </section>

  <section class="card card-back">
    <div class="pattern" role="img" aria-label="Repeating embossed brand pattern in tonal greys"></div>
    <div class="back-brand">
      <span class="brand-mark"></span>
      <span class="brand-name">Thornley Pike<br>Construction</span>
    </div>
  </section>
</main>
</body>
</html>
```